Wine business webpage
Italian fine wines
Project: Wine business webpage
Wine business webpage -
Creative Brief
Fine and Rare Italian wine merchant
Cantina del Sole specializes in the Italy's fine and rare wines. We have special relationships with many of the greatest estates and their distributors, and are able to pass on the benefits of those relationships to our customers. We would welcome the opportunity to put our passion and knowledge to work for you!
Dislike: homepage with loads of bottles of wine, e.g. http://www.vintageharborcellars.example/
Nature
natural wood
green - Terre Verte
earth tone
top
http://www.marlowecask.example/
http://www.grapeledgerhub.example/
http://www.vinoquay.example/

```html
<!DOCTYPE html>
<html lang="en">
<head>
<meta charset="utf-8">
<title>Cantina del Sole – Fine and Rare Italian Wines</title>
<link rel="stylesheet" href="https://fonts.googleapis.com/css2?family=Cabin:wght@400;600&display=swap">
<style>
  :root {
    --wood-dark: #3b2417;
    --wood-mid: #5a3a26;
    --wood-light: #6e4a31;
    --logo-top: #7a2c19;
    --logo-bottom: #4b1a0f;
    --cream: #f3e4c4;
    --tab: #e6cfa3;
    --tab-edge: #c9a877;
    --tab-active: #c47b36;
    --parchment: #ead7b2;
    --parchment-deep: #dcc196;
    --panel-frame: #cfb285;
    --ink: #4a2c1b;
    --ink-soft: #6b4b35;
    --heading: #5a3522;
    --dark-box: #2b2522;
    --dark-box-edge: #171312;
    --muted-light: #cfc4b4;
    --button: #3a312c;
  }
  * { margin: 0; padding: 0; box-sizing: border-box; }
  html, body { width: 1200px; height: 1064px; overflow: hidden; }
  body {
    font-family: "Cabin", sans-serif;
    color: var(--ink);
    background:
      repeating-linear-gradient(90deg, rgba(0,0,0,0.06) 0 3px, transparent 3px 11px, rgba(255,255,255,0.03) 11px 13px, transparent 13px 27px),
      linear-gradient(180deg, var(--wood-light) 0%, var(--wood-mid) 40%, var(--wood-dark) 100%);
  }
  .page { position: relative; width: 1200px; height: 1064px; }

  .brand {
    position: absolute; left: 63px; top: 0; width: 283px; height: 245px; z-index: 3;
    background: linear-gradient(180deg, var(--logo-top), var(--logo-bottom));
    box-shadow: 0 4px 14px rgba(0,0,0,0.45);
    display: flex; align-items: center; justify-content: center;
  }
  .brand-name { font-size: 30px; font-weight: 600; color: var(--cream); letter-spacing: 0.5px; }

  .main-nav { position: absolute; top: 0; left: 591px; display: flex; gap: 14px; z-index: 2; }
  .main-nav a {
    display: flex; align-items: flex-end; justify-content: center;
    width: 101px; height: 87px; padding-bottom: 16px;
    background: linear-gradient(180deg, var(--tab), #dcc191);
    border: 1px solid var(--tab-edge); border-top: none;
    color: var(--ink); font-size: 16px; text-decoration: none;
    box-shadow: 0 3px 8px rgba(0,0,0,0.35);
  }
  .main-nav a.is-current { background: linear-gradient(180deg, #d38d46, var(--tab-active)); color: #fff3dc; }

  .content-panel {
    position: absolute; left: 164px; top: 121px; width: 866px; height: 840px; z-index: 1;
    background: linear-gradient(180deg, var(--parchment), var(--parchment-deep));
    border: 5px solid var(--panel-frame);
    box-shadow: 0 6px 20px rgba(0,0,0,0.5);
  }
  .hero {
    position: absolute; left: 0; top: 0; width: 856px; height: 379px;
    background:
      radial-gradient(ellipse at 30% 45%, rgba(150,40,40,0.75), transparent 45%),
      radial-gradient(ellipse at 72% 55%, rgba(40,10,10,0.85), transparent 40%),
      radial-gradient(ellipse at 90% 80%, rgba(220,190,140,0.7), transparent 35%),
      linear-gradient(100deg, #e7d7bf 0%, #b07a55 25%, #6d2a22 55%, #3a1a14 75%, #c8a578 100%);
  }

  .welcome { position: absolute; left: 36px; top: 418px; font-size: 20px; font-weight: 600; color: var(--heading); }
  .section-title { position: absolute; left: 15px; font-size: 19px; font-weight: 600; color: var(--heading); }
  .about-title { top: 450px; }
  .wines-title { top: 610px; }
  .copy { position: absolute; font-size: 11.5px; line-height: 1.45; color: var(--ink-soft); }
  .copy p + p { margin-top: 9px; }
  .about-copy { left: 15px; top: 480px; width: 555px; }

  .wines-photo {
    position: absolute; left: 15px; top: 650px; width: 100px; height: 105px;
    background: radial-gradient(circle at 60% 40%, #c28b5c, transparent 55%), linear-gradient(135deg, #3a1a12, #7b3a24 55%, #d8b48a);
    border: 3px solid #f5ead2;
  }
  .wines-copy { left: 135px; top: 648px; width: 435px; }
  .read-more {
    position: absolute; padding: 3px 12px; border-radius: 10px;
    background: var(--button); color: #efe5d5; font-size: 11px; text-decoration: none;
  }
  .wines-more { left: 475px; top: 806px; }

  .activities {
    position: absolute; left: 587px; top: 408px; width: 260px; height: 418px;
    background: linear-gradient(180deg, #3a322d, var(--dark-box));
    border: 2px solid var(--dark-box-edge); border-radius: 6px;
    color: var(--muted-light);
  }
  .activities h2 { position: absolute; left: 18px; top: 18px; font-size: 20px; font-weight: 400; color: #f0e6d6; }
  .activity { position: absolute; left: 14px; width: 228px; }
  .activity-1 { top: 60px; }
  .activity-2 { top: 218px; }
  .activity-media { position: relative; height: 66px; background: #0d0b0a; border: 1px solid #4a413a; }
  .activity-thumb { position: absolute; right: 6px; top: 6px; width: 52px; height: 52px; }
  .activity-1 .activity-thumb { background: linear-gradient(135deg, #e8d6b0, #b5462c 60%, #6b2a18); }
  .activity-2 .activity-thumb { background: linear-gradient(135deg, #f0e2c0, #c69a5a 55%, #5a3a20); }
  .activity p { margin-top: 10px; font-size: 11px; line-height: 1.45; color: var(--muted-light); }
  .activity .read-more { position: static; display: inline-block; margin: 6px 0 0 150px; background: #5a524c; }

  .site-footer { position: absolute; left: 0; top: 985px; width: 1200px; height: 79px; background: linear-gradient(180deg, rgba(0,0,0,0.15), rgba(0,0,0,0.3)); }
  .site-footer small { display: block; margin-top: 40px; text-align: center; font-size: 11px; color: #b99a7a; }
</style>
</head>
<body>
<div class="page">
  <header>
    <div class="brand"><span class="brand-name">Cantina del Sole</span></div>
    <nav class="main-nav">
      <a href="#" class="is-current">Home</a>
      <a href="#">About Us</a>
      <a href="#">Specials</a>
      <a href="#">Wines</a>
    </nav>
  </header>

  <main class="content-panel">
    <div class="hero" role="img" aria-label="Glasses of red wine beside bottles and cheese on a warm table"></div>

    <h1 class="welcome">Welcome To Cantina del Sole...</h1>

    <h2 class="section-title about-title">About Us</h2>
    <div class="copy about-copy">
      <p>We source fine and rare wines from the great estates of Italy, working closely with growers and their distributors to bring each bottle to your table in perfect condition. Every wine is tasted, stored and shipped with care.</p>
      <p>Our cellar holds Barolo, Brunello and Amarone from celebrated vintages alongside quiet finds from small family farms. We are glad to guide collectors and first-time buyers alike.</p>
      <p>Ask us about private tastings, cellar planning and gifts for every occasion.</p>
    </div>

    <h2 class="section-title wines-title">Our Wines</h2>
    <div class="wines-photo" role="img" aria-label="Bottles of Italian red wine with a filled glass"></div>
    <div class="copy wines-copy">
      <p>Reds from Piedmont and Tuscany lead our list, chosen for depth, balance and the promise of many good years in the bottle.</p>
      <p>Crisp whites from Friuli and the Alto Adige bring fresh fruit and mineral notes, ideal with fish, pasta and summer evenings on the terrace.</p>
      <p>Sweet and sparkling wines round out the range, from Moscato d'Asti to rare Vin Santo.</p>
    </div>
    <a href="#" class="read-more wines-more">Read more</a>

    <aside class="activities">
      <h2>Activities</h2>
      <div class="activity activity-1">
        <div class="activity-media"><div class="activity-thumb" role="img" aria-label="Wine glasses at a tasting evening"></div></div>
        <p>Join our monthly tasting evenings with winemakers from across Italy and discover new favourites.</p>
        <a href="#" class="read-more">Read more</a>
      </div>
      <div class="activity activity-2">
        <div class="activity-media"><div class="activity-thumb" role="img" aria-label="Wine served with food at a pairing class"></div></div>
        <p>Cellar tours and food pairing classes run every season for small groups of friends.</p>
        <a href="#" class="read-more">Read more</a>
      </div>
    </aside>
  </main>

  <footer class="site-footer">
    <small>Copyright © 2011 Cantina del Sole. All Rights Reserved</small>
  </footer>
</div>
</body>
</html>
```